| バナーサイズ |
| 現在のヘッダーデザインにとらわれず、サイトイメージとマッチするような、 オリジナルのヘッダーを作成して下さい。 ■サイズ ヘッダー画像サイズ:横幅1450px、縦幅680px 対象サイト:http://www.vormeta-k.com ■会社(サービス)概要 企業向けのコンサルティングサービス、各種ビジネスサービスを展開しています。 主に中小企業、中堅企業向けのクライアントが対象 ■利用客層 男性メイン 特に、課長/部長等のマネージメントクラス、役員/経営者向け ■最後に ご質問あれば、回答させて頂きます。 一人で複数の応募も問題ございません。 多くの方からの、ご応募をお待ちしています。 |

```html
<!DOCTYPE html>
<html lang="ja">
<head>
<meta charset="utf-8">
<title>経験豊富な実践型エキスパートが戦略的事業創造と新産業創出をハンズオンで支援</title>
<link rel="stylesheet" href="https://fonts.googleapis.com/css2?family=Noto+Sans+JP:wght@700;900&display=swap">
<style>
  :root {
    --sky-top: #2c2f5e;
    --sky-mid: #6a5fa8;
    --sky-glow: #b7a6d9;
    --city-dark: #141a2a;
    --suit-dark: #1c1f2b;
    --text-main: #ffffff;
    --text-shadow: rgba(10, 12, 40, 0.75);
  }
  html, body {
    margin: 0;
    padding: 0;
    width: 1200px;
    height: 562px;
    overflow: hidden;
    background: var(--city-dark);
  }
  .header-banner {
    position: relative;
    width: 1200px;
    height: 562px;
    overflow: hidden;
    font-family: "Noto Sans JP", sans-serif;
    color: var(--text-main);
  }
  .header-banner__scene {
    position: absolute;
    inset: 0;
    background:
      radial-gradient(ellipse 520px 300px at 620px 200px, var(--sky-glow) 0%, rgba(183,166,217,0) 70%),
      linear-gradient(90deg, var(--suit-dark) 0%, rgba(28,31,43,0.55) 22%, rgba(28,31,43,0) 40%, rgba(28,31,43,0) 66%, rgba(28,31,43,0.6) 82%, var(--suit-dark) 100%),
      linear-gradient(180deg, var(--sky-top) 0%, var(--sky-mid) 38%, #4b4f7e 62%, var(--city-dark) 100%);
  }
  .header-banner__copy {
    position: absolute;
    inset: 0;
    text-shadow: 0 2px 4px var(--text-shadow), 0 0 10px var(--text-shadow);
  }
  .copy-line {
    position: absolute;
    margin: 0;
    white-space: nowrap;
    line-height: 1;
    letter-spacing: 0.02em;
  }
  .copy-line--lead {
    left: 340px;
    top: 74px;
    font-size: 32px;
    font-weight: 700;
  }
  .copy-line--headline {
    font-size: 54px;
    font-weight: 900;
  }
  .copy-line--headline-first {
    left: 336px;
    top: 136px;
  }
  .copy-line--headline-second {
    left: 498px;
    top: 220px;
  }
  .copy-line--tagline {
    left: 588px;
    top: 304px;
    font-size: 23px;
    font-weight: 700;
  }
</style>
</head>
<body>
  <header class="header-banner">
    <div class="header-banner__scene" role="img" aria-label="高層ビル街と紫がかった夕空を背景に、スーツ姿のビジネスマン二人が握手を交わす写真"></div>
    <div class="header-banner__copy">
      <p class="copy-line copy-line--lead">経験豊富な実践型エキスパートが</p>
      <h1 class="copy-line copy-line--headline copy-line--headline-first">戦略的事業創造と</h1>
      <p class="copy-line copy-line--headline copy-line--headline-second">新産業創出を</p>
      <p class="copy-line copy-line--tagline">ハンズオンで支援</p>
    </div>
  </header>
</body>
</html>
```